Design a Professional Business Card for Velmora Arcs

Design a business card for Velmora Arcs, we are a National Sport Court Company.

West Region Address: 4175 Quill Harbor Ln, Suite #215 Englewood, Colorado 80467
East Region Address: 3817 Tamsin Rd E, Bradenton, Florida 34583

Target Market(s)

High End Residential & Institutional Clients

Industry/Entity Type

Design & Construction

Contact Information for Business Card

Logo/Brand/Colors/ name, number (provided in comments)

Requirements
Must have
• Colors only provided in logo
Should not have
• Any other colors not in existing logo (attached)

```html
<!DOCTYPE html>
<html lang="en">
<head>
<meta charset="utf-8">
<title>Velmora Arcs – Business Card</title>
<link rel="stylesheet" href="https://fonts.googleapis.com/css2?family=Jost:wght@400;500;700&display=swap">
<style>
  :root{
    --navy:#1b3a6e;
    --green:#16803d;
    --teal:#0f5a56;
    --white:#ffffff;
    --grey-text:#5b5f66;
    --paper:#f7f8f8;
    --stage:#e9eaec;
    --faint:#dfe3e6;
  }
  *{box-sizing:border-box;margin:0;padding:0}
  html,body{width:1200px;height:900px;overflow:hidden}
  body{background:var(--stage);font-family:"Jost",sans-serif;position:relative}

  .card{position:absolute;left:290px;width:620px;height:354px;border-radius:34px;overflow:hidden;box-shadow:0 10px 30px rgba(0,0,0,.18)}

  /* back side */
  .card-back{top:52px;background:radial-gradient(ellipse at 50% 45%,var(--green) 0%,var(--teal) 40%,var(--navy) 85%);color:var(--white)}
  .back-mark{position:absolute;left:0;right:0;top:78px;display:flex;flex-direction:column;align-items:center;gap:14px}
  .back-mark .dot{width:84px;height:84px;border-radius:50%;background:var(--white)}
  .back-mark .brand{font-size:26px;font-weight:700;letter-spacing:3px;text-transform:uppercase;color:var(--white)}
  .back-rule{position:absolute;left:70px;right:70px;top:242px;height:1px;background:linear-gradient(90deg,transparent,rgba(255,255,255,.75),transparent)}
  .addresses{position:absolute;left:0;right:0;top:260px;text-align:center;font-size:14.5px;line-height:26px;letter-spacing:.3px}
  .addresses svg{width:11px;height:14px;vertical-align:-2px;margin-right:6px;fill:var(--white)}

  /* front side */
  .card-front{top:476px;background:linear-gradient(160deg,var(--white) 0%,var(--paper) 100%)}
  .front-deco{position:absolute;left:40px;top:150px;width:300px;height:300px;border-radius:50%;background:linear-gradient(135deg,var(--faint),#e6ece8)}
  .person{position:absolute;left:38px;top:48px}
  .person .name{font-size:22px;font-weight:700;color:var(--navy);letter-spacing:.5px;text-transform:uppercase}
  .person .role{font-size:17px;color:var(--grey-text);margin-top:2px}
  .contact{position:absolute;left:372px;top:48px;list-style:none;font-size:15px;color:var(--navy);line-height:27px}
  .contact svg{width:14px;height:14px;vertical-align:-2px;margin-right:8px;fill:none;stroke:var(--navy);stroke-width:1.6}
  .front-rule{position:absolute;left:372px;right:40px;top:172px;height:2px;background:var(--green)}
  .front-mark{position:absolute;right:40px;top:208px;display:flex;align-items:center;gap:16px}
  .front-mark .dot{width:78px;height:78px;border-radius:50%;background:var(--navy)}
  .front-mark .brand{font-size:34px;font-weight:700;line-height:36px;letter-spacing:4px;text-transform:uppercase;color:var(--navy)}
</style>
</head>
<body>

<section class="card card-back">
  <div class="back-mark">
    <span class="dot"></span>
    <span class="brand">Velmora Arcs</span>
  </div>
  <div class="back-rule"></div>
  <div class="addresses">
    <p><svg viewBox="0 0 10 14"><path d="M5 0a5 5 0 0 0-5 5c0 3.5 5 9 5 9s5-5.5 5-9a5 5 0 0 0-5-5zm0 7a2 2 0 1 1 0-4 2 2 0 0 1 0 4z"/></svg>West Region - 4175 Quill Harbor Ln, Suite #215 Englewood, Colorado 80467</p>
    <p><svg viewBox="0 0 10 14"><path d="M5 0a5 5 0 0 0-5 5c0 3.5 5 9 5 9s5-5.5 5-9a5 5 0 0 0-5-5zm0 7a2 2 0 1 1 0-4 2 2 0 0 1 0 4z"/></svg>East Region - 3817 Tamsin Rd E, Bradenton, Florida 34583</p>
  </div>
</section>

<section class="card card-front">
  <div class="front-deco"></div>
  <div class="person">
    <p class="name">Dorian M. Feld, ASLA</p>
    <p class="role">CEO &amp; Founder</p>
  </div>
  <ul class="contact">
    <li><svg viewBox="0 0 14 14"><rect x="3.5" y="1" width="7" height="12" rx="1.2"/></svg>(303) 555-0147</li>
    <li><svg viewBox="0 0 14 14"><path d="M3 1.5l2 2.5-1 1.5a7 7 0 0 0 4.5 4.5l1.5-1 2.5 2-1.2 1.5C6 12 2 8 1.5 2.7z"/></svg>1-800-555-0193</li>
    <li><svg viewBox="0 0 14 14"><rect x="1" y="3" width="12" height="8"/><path d="M1 3l6 5 6-5"/></svg>dorian@velmoraarcs.com</li>
    <li><svg viewBox="0 0 14 14"><circle cx="7" cy="7" r="6"/><path d="M1 7h12M7 1c-3 3.5-3 8.5 0 12M7 1c3 3.5 3 8.5 0 12"/></svg>www.velmoraarcs.com</li>
  </ul>
  <div class="front-rule"></div>
  <div class="front-mark">
    <span class="dot"></span>
    <span class="brand">Velmora<br>Arcs</span>
  </div>
</section>

</body>
</html>
```